Admin Backend Redesign

We need a redesign for our backend which supoosed to make the backoffice look more modern!

I will add screenshots of the backoffice so you know what data will be shown in the Admin.

Have in mind that the users of this backend are Doctors. We need a clinical look, modern and sharp. The backoffice is responsive, have that in mind. We need the backoffice to look as professional as possible.

The theme used for the website is: http://velmora.quillstack-sample.com/

ON the main page of the backoffice, under every widget i need some space to write an explanation what the widget is about.

The color code used in our logo and website is #57aad4 combined with white.

We are open for ideas!
Updates

Project Deadline Extended
Reason: Designs are ok, but nothing innovative. Please use more modern designs!

Project Deadline Extended
Reason: Havent recieved a perfect design yet. Please read instructions carefully! Thank you

Project Deadline Extended
Reason: Hey everybody, sorry for the delay. We will decide in 3 days. If anyone wants to add a Design, that would be great.

Target Market(s)

Doctors, therapists

Industry/Entity Type

It Professional

Font styles to use
Sans Serif

Requirements
Must have
• Must look uptodate, modern, like new back offices look nowadays

```html
<!DOCTYPE html>
<html lang="de">
<head>
<meta charset="utf-8">
<title>Dashboard – Dr. Musterman</title>
<link rel="stylesheet" href="https://fonts.googleapis.com/css2?family=Raleway:wght@400;500;600;700;800&display=swap">
<style>
  :root {
    --page-bg: #e2f1f1;
    --panel: #ffffff;
    --tab-grey: #e4e4e4;
    --tab-grey-dark: #d2d2d2;
    --ink: #1f1f1f;
    --muted: #8a8a8a;
    --green-top: #8fcf3a;
    --green-bottom: #5ca61e;
    --patients-top: #fff7cf;
    --patients-bottom: #e6f4cf;
    --btn-blue: #bfe3df;
    --btn-orange: #f7a13a;
    --chart-top: #fbb03b;
    --chart-bottom: #f27a24;
    --charts-bg: #fdf5e2;
    --red: #e2452f;
    --orange: #f29a2e;
    --photo: #c9d8e4;
  }
  * { box-sizing: border-box; margin: 0; padding: 0; }
  html, body { width: 1200px; height: 800px; overflow: hidden; }
  body {
    background: var(--page-bg);
    font-family: "Raleway", Arial, sans-serif;
    color: var(--ink);
  }
  .panel {
    position: absolute;
    left: 170px; top: 0;
    width: 860px; height: 800px;
    background: var(--panel);
    overflow: hidden;
  }
  .tabs { display: flex; height: 64px; }
  .tab {
    flex: 1;
    display: flex; align-items: center; gap: 12px;
    padding: 0 22px;
    font-size: 14px; font-weight: 500;
    background: var(--tab-grey);
    color: #444;
  }
  .tab--active { background: var(--panel); }
  .tab--last { background: var(--tab-grey-dark); }
  .tab-icon {
    width: 26px; height: 26px; border-radius: 50%;
    background: #f1f1f1; border: 1px solid #d6d6d6;
    display: flex; align-items: center; justify-content: center;
  }
  .header {
    display: flex; justify-content: space-between; align-items: flex-start;
    padding: 32px 26px 0 50px;
  }
  .profile { display: flex; gap: 18px; }
  .profile-photo {
    width: 108px; height: 108px; background: linear-gradient(160deg, #e7eef3, var(--photo));
    border: 3px solid #fff; box-shadow: 0 0 0 1px #ddd;
  }
  .welcome { font-size: 18px; font-weight: 500; color: #444; }
  .doctor-name { font-size: 30px; font-weight: 800; margin-top: 2px; letter-spacing: -0.3px; }
  .status-label { font-size: 11px; color: var(--muted); margin-top: 8px; }
  .profile-actions { display: flex; align-items: center; gap: 26px; margin-top: 6px; }
  .status-btn {
    width: 140px; height: 30px; border-radius: 3px;
    background: linear-gradient(var(--green-top), var(--green-bottom));
    color: #fff; font-size: 11px; font-weight: 700;
    display: flex; align-items: center; justify-content: space-between; padding: 0 10px;
  }
  .edit-profile { display: flex; align-items: center; gap: 12px; font-size: 12px; color: #555; }
  .patients-card {
    width: 262px; height: 150px; margin-top: -8px;
    background: linear-gradient(var(--patients-top), var(--patients-bottom));
    border-radius: 6px; padding: 20px 18px;
  }
  .patients-label { font-size: 12px; color: #666; }
  .patients-count { font-size: 22px; font-weight: 700; margin-top: 4px; }
  .patients-actions { display: flex; gap: 14px; margin-top: 26px; }
  .patients-btn {
    flex: 1; height: 34px; border-radius: 4px;
    font-size: 11px; font-weight: 600;
    display: flex; align-items: center; justify-content: center;
  }
  .patients-btn--view { background: var(--btn-blue); color: #4a6f6c; }
  .patients-btn--add { background: var(--btn-orange); color: #fff; }
  .trend-card {
    position: absolute; left: 50px; top: 300px;
    width: 810px; height: 365px; border-radius: 8px;
    background: linear-gradient(var(--chart-top), var(--chart-bottom));
    box-shadow: 0 6px 14px rgba(200, 90, 20, 0.35);
    overflow: hidden;
  }
  .trend-title {
    position: absolute; left: 30px; top: 26px;
    display: flex; align-items: center; gap: 20px;
    color: #fff; font-size: 13px; font-weight: 600;
  }
  .trend-settings {
    position: absolute; right: 24px; top: 24px;
    width: 22px; height: 22px; border-radius: 50%;
    border: 2px solid rgba(255,255,255,0.8);
  }
  .trend-chart { position: absolute; left: 0; top: 0; }
  .charts-card {
    position: absolute; left: 50px; top: 700px;
    width: 810px; height: 140px; border-radius: 6px;
    background: var(--charts-bg); padding: 26px 30px;
  }
  .charts-head { display: flex; align-items: center; gap: 14px; color: var(--red); font-size: 16px; font-weight: 600; }
  .charts-tabs { display: flex; gap: 40px; margin-top: 14px; font-size: 14px; font-weight: 800; }
  .charts-tab--active { color: var(--red); border-bottom: 3px solid var(--red); padding-bottom: 4px; }
  .charts-tab { color: var(--orange); }
  .charts-settings {
    position: absolute; right: 26px; top: 26px;
    width: 18px; height: 18px; border-radius: 50%; border: 2px solid #c9c0a8;
  }
</style>
</head>
<body>
<div class="panel">
  <nav class="tabs">
    <div class="tab tab--active">
      <span class="tab-icon"><svg width="12" height="12" viewBox="0 0 12 12"><path d="M1 6 L6 1.5 L11 6 M2.5 5 V10.5 H9.5 V5" fill="none" stroke="#555" stroke-width="1.4"/></svg></span>
      Dashboard
    </div>
    <div class="tab">
      <svg width="16" height="14" viewBox="0 0 16 14"><rect x="1" y="2" width="14" height="11" fill="none" stroke="#555" stroke-width="1.4"/><path d="M1 6 H15" stroke="#555" stroke-width="1.4"/></svg>
      Mein Conto
    </div>
    <div class="tab tab--last">
      <span class="tab-icon"><svg width="12" height="12" viewBox="0 0 12 12"><circle cx="6" cy="4" r="2.5" fill="none" stroke="#555" stroke-width="1.3"/><path d="M1.5 11.5 C2 8 10 8 10.5 11.5" fill="none" stroke="#555" stroke-width="1.3"/></svg></span>
      Patientenbewertungen
    </div>
  </nav>

  <section class="header">
    <div class="profile">
      <div class="profile-photo" role="img" aria-label="Profilfoto des Arztes"></div>
      <div class="profile-info">
        <p class="welcome">Willkommen</p>
        <h1 class="doctor-name">Dr. Musterman</h1>
        <p class="status-label">Ihr Status</p>
        <div class="profile-actions">
          <div class="status-btn"><span>Aktiv</span>
            <svg width="8" height="6" viewBox="0 0 8 6"><path d="M0 0 H8 L4 6 Z" fill="#fff"/></svg>
          </div>
          <div class="edit-profile">
            <svg width="16" height="16" viewBox="0 0 16 16"><circle cx="8" cy="8" r="5" fill="none" stroke="#666" stroke-width="2.5" stroke-dasharray="2.5 1.4"/><circle cx="8" cy="8" r="2" fill="#666"/></svg>
            Edit Profile
          </div>
        </div>
      </div>
    </div>
    <aside class="patients-card">
      <p class="patients-label">Patient verwalten</p>
      <p class="patients-count">6 Patients</p>
      <div class="patients-actions">
        <span class="patients-btn patients-btn--view">Alle Ansehen</span>
        <span class="patients-btn patients-btn--add">Add Patient</span>
      </div>
    </aside>
  </section>

  <section class="trend-card">
    <svg class="trend-chart" width="810" height="365" viewBox="0 0 810 365">
      <g stroke="rgba(255,255,255,0.35)" stroke-width="1">
        <line x1="30" y1="140" x2="780" y2="140"/>
        <line x1="30" y1="210" x2="780" y2="210"/>
        <line x1="30" y1="280" x2="780" y2="280"/>
      </g>
      <path d="M50 320 L83 221 L129 242 L182 149 L231 185 L304 161 L347 272 L377 251 L430 263 L463 209 L499 185 L549 119 L615 74 L681 134 L730 107 L757 215 L757 320 Z" fill="rgba(255,255,255,0.28)"/>
      <polyline points="50,320 83,221 129,242 182,149 231,185 304,161 347,272 377,251 430,263 463,209 499,185 549,119 615,74 681,134 730,107 757,215" fill="none" stroke="#fff" stroke-width="3" stroke-linejoin="round"/>
      <g fill="#fff">
        <circle cx="83" cy="221" r="5"/><circle cx="129" cy="242" r="5"/><circle cx="182" cy="149" r="5"/>
        <circle cx="231" cy="185" r="5"/><circle cx="304" cy="161" r="5"/><circle cx="347" cy="272" r="5"/>
        <circle cx="377" cy="251" r="5"/><circle cx="430" cy="263" r="5"/><circle cx="463" cy="209" r="5"/>
        <circle cx="499" cy="185" r="5"/><circle cx="549" cy="119" r="5"/><circle cx="615" cy="74" r="5"/>
        <circle cx="681" cy="134" r="5"/><circle cx="730" cy="107" r="5"/>
      </g>
      <g fill="rgba(255,255,255,0.85)" font-family="Raleway, Arial, sans-serif" font-size="11">
        <text x="40" y="143">18</text><text x="40" y="213">12</text><text x="40" y="283">6</text>
        <text x="190" y="335">Jul 2012</text><text x="330" y="335">Oct 2012</text>
        <text x="460" y="335">Jan 2014</text><text x="600" y="335">Apr 2014</text>
      </g>
    </svg>
    <div class="trend-title">
      <svg width="22" height="18" viewBox="0 0 22 18"><path d="M1 1 V17 H21" fill="none" stroke="#fff" stroke-width="2"/><path d="M5 12 L10 7 L13 10 L19 4" fill="none" stroke="#fff" stroke-width="2"/></svg>
      Sys Trend Für
    </div>
    <span class="trend-settings"></span>
  </section>

  <section class="charts-card">
    <div class="charts-head">
      <svg width="18" height="18" viewBox="0 0 18 18"><rect x="1" y="8" width="4" height="9" fill="#e2452f"/><rect x="7" y="3" width="4" height="14" fill="#e2452f"/><rect x="13" y="6" width="4" height="11" fill="#e2452f"/></svg>
      Charts
    </div>
    <div class="charts-tabs">
      <span class="charts-tab--active">PIE CHART 2013</span>
      <span class="charts-tab">PIE CHART 2014</span>
    </div>
    <span class="charts-settings"></span>
  </section>
</div>
</body>
</html>
```